KelvrasMassage website required

We need a website for a mobile sports massage therapist in the United Kingdom. Specialising in pregnancy and postnatal massage, sports and remedial, deep tissue massage & Corprate Massage. Attached are some logos that we already have in various colours. The file named logo_white_background is what we normally use. Feel free to use the others at your discretion.

Requirements
Must have
• Service areas, Booking system.

```html
<!DOCTYPE html>
<html lang="en">
<head>
<meta charset="utf-8">
<title>Kelvra's Massage</title>
<link href="https://fonts.googleapis.com/css2?family=Jost:wght@400;500;600&family=Montserrat:wght@400;500;600&display=swap" rel="stylesheet">
<style>
:root{
  --blue:#4aaee8;
  --blue-band:#5db4e4;
  --orange:#f07b1f;
  --ink:#222;
  --muted:#555;
  --dark:#161616;
  --cream:#f7f1ea;
  --white:#fff;
}
*{margin:0;padding:0;box-sizing:border-box}
html,body{width:1200px;height:3974px;overflow:hidden}
body{position:relative;font-family:"Montserrat",sans-serif;color:var(--ink);background:var(--white)}
.abs{position:absolute}
h1,h2,h3,.nav,.brand{font-family:"Jost",sans-serif;font-weight:500}
.btn-orange{background:var(--orange);color:#fff;border-radius:22px;font-family:"Jost",sans-serif;font-weight:500;display:flex;align-items:center;justify-content:center}
.btn-outline{border:2px solid var(--ink);border-radius:20px;font-size:12px;font-weight:600;letter-spacing:.5px;display:flex;align-items:center;justify-content:center}

/* header */
.site-header{top:0;left:0;width:1200px;height:120px;background:#fff;z-index:2}
.logo-badge{left:112px;top:-30px;width:200px;height:200px;border-radius:50%;background:#fff;z-index:3;display:flex;align-items:center;justify-content:center}
.brand{font-size:30px;color:var(--blue);text-align:center;line-height:1.1}
.call{left:540px;top:24px;font-family:"Jost",sans-serif;font-size:19px;color:#333;display:flex;align-items:center;gap:10px}
.call span{color:var(--blue)}
.header-btn{left:866px;top:16px;width:200px;height:40px;font-size:17px}
.nav{left:392px;top:72px;width:700px;font-size:19px;color:#222}
.nav a{position:absolute;white-space:nowrap;text-decoration:none;color:inherit}

/* hero */
.hero{top:120px;left:0;width:1200px;height:680px;background:linear-gradient(100deg,#6a4430 0%,#a9775a 40%,#d3a88a 70%,#b6866a 100%)}
.hero h1{left:132px;top:180px;font-size:58px;color:#fff;font-weight:500}
.hero p{left:132px;top:268px;width:470px;font-size:16px;line-height:26px;color:#fff}
.hero-btn{left:132px;top:372px;width:210px;height:46px;font-size:18px}
.arrow{top:305px;width:36px;height:36px;border-radius:50%;background:rgba(0,0,0,.55);display:flex;align-items:center;justify-content:center}
.hero-wave{left:0;top:600px}

/* welcome */
.welcome-photo{left:132px;top:845px;width:350px;height:350px;border-radius:50%;border:6px solid var(--blue);padding:8px;background:#fff}
.welcome-photo div{width:100%;height:100%;border-radius:50%;background:radial-gradient(circle at 45% 40%,#e8b896,#b67a57 70%,#8a5a40)}
.welcome h2{left:525px;top:860px;font-size:44px;color:#111}
.welcome h2 span{color:var(--blue)}
.welcome p{left:525px;top:935px;width:545px;font-size:14px;line-height:26px;color:var(--muted)}
.welcome .btn-outline{left:525px;top:1130px;width:112px;height:34px}

/* features */
.features{top:1295px;left:0;width:1200px;height:415px;background:linear-gradient(180deg,#62b8e8,#4eaadf)}
.feature{top:80px;width:320px;text-align:center;color:#fff}
.feature .icon{width:104px;height:104px;border-radius:50%;background:#555;margin:0 auto;display:flex;align-items:center;justify-content:center}
.feature h3{font-size:23px;font-weight:400;margin-top:24px}
.feature p{font-size:13px;line-height:21px;margin:12px 20px 0}
.feature .chev{margin-top:18px}

/* services */
.services{top:1710px;left:0;width:1200px;height:865px;background:radial-gradient(ellipse at 50% 40%,#2b2b2b,#0d0d0d 80%)}
.services h2{top:85px;width:1200px;text-align:center;font-size:42px;color:#fff}
.tile{width:303px;height:246px;border:3px solid var(--blue)}
.tile .label{position:absolute;left:0;bottom:0;width:100%;height:40px;background:rgba(20,20,20,.75);color:#fff;font-family:"Jost",sans-serif;font-size:19px;display:flex;align-items:center;justify-content:center}

/* sports */
.sports h2{left:132px;top:2680px;font-size:40px;color:#111}
.sports p{left:132px;top:2750px;width:440px;font-size:14px;line-height:26px;color:var(--muted)}
.sports .btn-outline{left:132px;top:2940px;width:112px;height:34px}
.runners{left:630px;top:2615px;width:440px;height:465px;background:linear-gradient(160deg,#e8d9cc,#b8563f 55%,#7a2e22);border-radius:40% 40% 30% 30%}

/* booking */
.booking{top:3085px;left:0;width:1200px;height:520px;background:var(--cream)}
.booking-photo{left:0;top:0;width:650px;height:500px;background:linear-gradient(90deg,#efe6dc,#d9b08c 45%,#8b5a3a 70%,#efe6dc)}
.booking h2{left:668px;top:175px;font-size:34px;color:#111;font-weight:500}
.field{left:668px;width:382px;height:38px;background:#fff;border:1px solid #ddd;font-size:12px;color:#888;padding-left:12px;display:flex;align-items:center}
.book-btn{left:668px;top:385px;width:106px;height:34px;background:var(--blue);color:#fff;font-size:12px;font-weight:600;display:flex;align-items:center;justify-content:center}
.booking-wave{left:0;top:440px}

/* footer */
.site-footer{top:3605px;left:0;width:1200px;height:369px;background:var(--dark);color:#fff}
.site-footer h4{font-family:"Jost",sans-serif;font-weight:600;font-size:17px;letter-spacing:.5px}
.contact-row{display:flex;gap:14px;font-size:12px;line-height:18px;align-items:flex-start}
.socials{display:flex;gap:8px}
.socials span{width:26px;height:26px;border:1.5px solid #fff;border-radius:50%}
.links li{list-style:none;font-size:12px;line-height:25px;display:flex;align-items:center;gap:10px}
.links li::before{content:"";width:9px;height:9px;border-radius:50%;background:#fff}
.news-text{font-size:12px;line-height:18px;width:270px}
.news-input{width:255px;height:36px;background:#fff;color:#888;font-size:11px;padding-left:12px;display:flex;align-items:center}
.sub-btn{width:110px;height:30px;background:var(--blue);font-size:12px;font-weight:600;display:flex;align-items:center;justify-content:center}
.footer-brand{left:880px;top:90px;width:200px;text-align:center;font-size:34px;color:#fff}
.bottom-bar{left:132px;top:305px;width:936px;border-top:1px solid #333;padding-top:14px;font-size:11px;display:flex;justify-content:space-between}
</style>
</head>
<body>

<header class="abs site-header">
  <div class="abs call">
    <svg width="18" height="18" viewBox="0 0 24 24"><path fill="#333" d="M6.6 10.8a15 15 0 0 0 6.6 6.6l2.2-2.2c.3-.3.7-.4 1-.2 1.1.4 2.3.6 3.6.6.6 0 1 .4 1 1V20c0 .6-.4 1-1 1A17 17 0 0 1 3 4c0-.6.4-1 1-1h3.5c.6 0 1 .4 1 1 0 1.3.2 2.5.6 3.6.1.3 0 .7-.2 1z"/></svg>
    Call Us Today: <span>+44 7700 900123</span>
  </div>
  <a class="abs btn-orange header-btn">make an appointment</a>
  <nav class="abs nav">
    <a style="left:0">Home</a>
    <a style="left:74px">About Us</a>
    <a style="left:172px">Our Services</a>
    <a style="left:302px">Book Appointment</a>
    <a style="left:472px">Packages</a>
    <a style="left:586px">Contact Us</a>
  </nav>
</header>
<div class="abs logo-badge"><div class="brand">Kelvra's<br>Massage</div></div>

<section class="abs hero">
  <div class="abs" role="img" aria-label="Woman relaxing during a massage" style="inset:0"></div>
  <h1 class="abs">Kelvra's Massage</h1>
  <p class="abs">We are a sports massage therapist in the United Kingdom. Specialising in pregnancy and postnatal massage, sports and remedial, deep tissue massage</p>
  <a class="abs btn-orange hero-btn">make an appointment</a>
  <div class="abs arrow" style="left:72px"><svg width="12" height="12" viewBox="0 0 12 12"><path d="M8 1 3 6l5 5" stroke="#fff" stroke-width="2" fill="none"/></svg></div>
  <div class="abs arrow" style="left:1090px"><svg width="12" height="12" viewBox="0 0 12 12"><path d="m4 1 5 5-5 5" stroke="#fff" stroke-width="2" fill="none"/></svg></div>
  <svg class="abs hero-wave" width="1200" height="80" viewBox="0 0 1200 80">
    <path d="M0 60 C300 10 700 10 1200 0 L1200 80 L0 80Z" fill="#fff"/>
    <path d="M0 55 C320 5 700 5 1200 -5" stroke="#4aaee8" stroke-width="8" fill="none"/>
    <path d="M0 72 C320 25 700 22 1200 14" stroke="#4aaee8" stroke-width="3" fill="none"/>
  </svg>
</section>

<section class="welcome">
  <div class="abs welcome-photo"><div role="img" aria-label="Hands massaging a back"></div></div>
  <h2 class="abs">Welcome to <span>Kelvra's Massage</span></h2>
  <p class="abs">Kelvra's Massage brings skilled, caring treatments to your home, office or club. Every session is shaped around your body, your goals and your schedule. Whether you are expecting, recovering after birth, training for an event or simply carrying tension from daily life, we listen first and then work with focus, warmth and proven technique to help you feel and move better.</p>
  <a class="abs btn-outline">READ MORE</a>
</section>

<section class="abs features">
  <div class="abs feature" style="left:102px">
    <div class="icon"><svg width="46" height="40" viewBox="0 0 46 40"><rect x="3" y="3" width="40" height="26" rx="2" fill="none" stroke="#fff" stroke-width="4"/><rect x="17" y="30" width="12" height="5" fill="#fff"/><rect x="11" y="35" width="24" height="3" fill="#fff"/></svg></div>
    <h3>Book Your Treatment</h3>
    <p>Choose a time that suits you and book your session online in just a few clicks.</p>
    <svg class="chev" width="16" height="16" viewBox="0 0 16 16"><path d="m2 2 6 5 6-5M2 9l6 5 6-5" stroke="#fff" stroke-width="2" fill="none"/></svg>
  </div>
  <div class="abs feature" style="left:441px">
    <div class="icon"><svg width="40" height="40" viewBox="0 0 40 40"><rect x="4" y="14" width="32" height="8" fill="#fff"/><rect x="7" y="24" width="26" height="14" fill="#fff"/><rect x="18" y="14" width="4" height="24" fill="#555"/><path d="M20 14c-4-8-12-8-10-2M20 14c4-8 12-8 10-2" stroke="#fff" stroke-width="3" fill="none"/></svg></div>
    <h3>Great Gift Packages</h3>
    <p>Treat someone special to a relaxing massage with a gift voucher for any occasion.</p>
    <svg class="chev" width="16" height="16" viewBox="0 0 16 16"><path d="m2 2 6 5 6-5M2 9l6 5 6-5" stroke="#fff" stroke-width="2" fill="none"/></svg>
  </div>
  <div class="abs feature" style="left:775px">
    <div class="icon"><svg width="42" height="42" viewBox="0 0 42 42"><path d="M4 4h16l18 18-16 16L4 20z" fill="#fff"/><circle cx="12" cy="12" r="3" fill="#555"/></svg></div>
    <h3>Special Offers &amp; Deals</h3>
    <p>Save on regular treatments with seasonal offers and great value multi session bundles.</p>
    <svg class="chev" width="16" height="16" viewBox="0 0 16 16"><path d="m2 2 6 5 6-5M2 9l6 5 6-5" stroke="#fff" stroke-width="2" fill="none"/></svg>
  </div>
</section>

<section class="abs services">
  <h2 class="abs">Our Services</h2>
  <div class="abs tile" style="left:132px;top:206px;background:linear-gradient(135deg,#e9d6c4,#c79a7a)" role="img" aria-label="Pregnancy massage treatment"><div class="label">Pregnancy Massage</div></div>
  <div class="abs tile" style="left:449px;top:206px;background:linear-gradient(135deg,#dfe6ea,#c9a48a)" role="img" aria-label="Postnatal massage treatment"><div class="label">Postnatal Massage</div></div>
  <div class="abs tile" style="left:766px;top:206px;background:linear-gradient(135deg,#eee,#d9a08a 60%,#e55)" role="img" aria-label="Sports massage on a leg"><div class="label">Sports Massage</div></div>
  <div class="abs tile" style="left:132px;top:468px;background:linear-gradient(135deg,#c79a7a,#8a5a3e)" role="img" aria-label="Remedial massage treatment"><div class="label">Remedial Massage</div></div>
  <div class="abs tile" style="left:449px;top:468px;background:linear-gradient(135deg,#b57a55,#5a3422)" role="img" aria-label="Deep tissue massage treatment"><div class="label">Deep Tissue Massage</div></div>
  <div class="abs tile" style="left:766px;top:468px;background:linear-gradient(135deg,#e6eef3,#c98a62)" role="img" aria-label="Relaxing treatment by the sea"><div class="label">Kelvras Massage</div></div>
</section>

<section class="sports">
  <h2 class="abs">Sports Massage Therapist</h2>
  <p class="abs">Our sports massage helps athletes of every level prepare, perform and recover. We target tight muscles, ease soreness and improve mobility so you can train harder and return from injury with confidence. Every session is tailored to your sport and your goals.</p>
  <a class="abs btn-outline">READ MORE</a>
  <div class="abs runners" role="img" aria-label="Anatomical illustration of running figures showing skeleton and muscles"></div>
</section>

<section class="abs booking">
  <div class="abs booking-photo" role="img" aria-label="Surprised woman pointing towards the booking form"></div>
  <h2 class="abs">Book An Appointment Now!</h2>
  <div class="abs field" style="top:238px">First Name</div>
  <div class="abs field" style="top:286px">Last Name</div>
  <div class="abs field" style="top:336px">Email</div>
  <a class="abs book-btn">BOOKING</a>
  <svg class="abs booking-wave" width="1200" height="80" viewBox="0 0 1200 80">
    <path d="M0 80 L0 50 C400 70 800 60 1200 0 L1200 80Z" fill="#161616"/>
    <path d="M0 44 C400 64 800 54 1200 -6" stroke="#4aaee8" stroke-width="8" fill="none"/>
    <path d="M0 30 C400 50 800 40 1200 -18" stroke="#4aaee8" stroke-width="3" fill="none"/>
  </svg>
</section>

<footer class="abs site-footer">
  <div class="abs" style="left:132px;top:45px">
    <h4>CONTACT US</h4>
    <div class="contact-row" style="margin-top:22px">
      <svg width="16" height="20" viewBox="0 0 16 20"><path d="M8 1a6 6 0 0 0-6 6c0 5 6 12 6 12s6-7 6-12a6 6 0 0 0-6-6z" fill="none" stroke="#fff" stroke-width="1.5"/><circle cx="8" cy="7" r="2" fill="#fff"/></svg>
      <span>Kelvra's Massage<br>24 Mill Lane, Ashbury, AB1 2CD</span>
    </div>
    <div class="contact-row" style="margin-top:12px">
      <svg width="16" height="16" viewBox="0 0 24 24"><path fill="#fff" d="M6.6 10.8a15 15 0 0 0 6.6 6.6l2.2-2.2c.3-.3.7-.4 1-.2 1.1.4 2.3.6 3.6.6.6 0 1 .4 1 1V20c0 .6-.4 1-1 1A17 17 0 0 1 3 4c0-.6.4-1 1-1h3.5c.6 0 1 .4 1 1 0 1.3.2 2.5.6 3.6.1.3 0 .7-.2 1z"/></svg>
      <span>Phone : +44 7700 900123</span>
    </div>
    <div class="contact-row" style="margin-top:12px">
      <svg width="18" height="14" viewBox="0 0 18 14"><rect x="1" y="1" width="16" height="12" fill="none" stroke="#fff" stroke-width="1.5"/><path d="m1 1 8 7 8-7" fill="none" stroke="#fff" stroke-width="1.5"/></svg>
      <span>Email: info@kelvrasmassage.com</span>
    </div>
    <div class="socials" style="margin-top:18px"><span></span><span></span><span></span><span></span><span></span></div>
  </div>
  <div class="abs" style="left:421px;top:45px">
    <h4>QUICK LINKS</h4>
    <ul class="links" style="margin-top:14px">
      <li>Home</li><li>About Us</li><li>Our Services</li><li>Pricing</li><li>Blog</li><li>Contact Us</li>
    </ul>
  </div>
  <div class="abs" style="left:588px;top:45px">
    <h4>SIGN UP FOR NEWSLETTER</h4>
    <p class="news-text" style="margin-top:18px">Sign up for news, offers and wellness tips sent to your inbox each month.</p>
    <div class="news-input" style="margin-top:16px">Enter email</div>
    <div class="sub-btn" style="margin-top:14px">SUBSCRIPTION</div>
  </div>
  <div class="abs brand footer-brand">Kelvra's<br>Massage</div>
  <div class="abs bottom-bar">
    <span>Copyright © 2018 Kelvra's Massage. All rights reserved.</span>
    <span>Contact Us &nbsp;/&nbsp; News &nbsp;/&nbsp; Terms Of Use &nbsp;/&nbsp; Privacy Policy</span>
  </div>
</footer>

</body>
</html>
```